Commercial photographer, UAV drone photography & 360 walk-through visuals

I need a business card design that is minimalist but yet pretentiously creative. My target market are architects, designers, advertising agents and marketing managers. It is important to stress that though I am asking for a minimalist design it needs to have creative impact.

Target Market(s)

Architects, interiors designers, web-designers, artists

Contact Information for Business Card

Include my name, mobile [cell] number, email, web page and the company logo. Do not to include a postal address.

Colors

Designer to choose colors to be used in the design.

Requirements
Must have
• The following information is to be included:
• Miles Perrow
• Photographer
• m: 07812 593174
• e: miles@mpframeworks.co.uk
• w: mpframeworks.co.uk

```html
<!DOCTYPE html>
<html lang="en">
<head>
<meta charset="utf-8">
<title>MP Frameworks — Business Card</title>
<link rel="stylesheet" href="https://fonts.googleapis.com/css2?family=Poppins:wght@300;400;500;600&display=swap">
<style>
  :root {
    --backdrop: #8fd3d5;
    --paper: #ffffff;
    --ink: #0b0b0c;
    --reverse-ink: #ffffff;
  }
  * { margin: 0; padding: 0; box-sizing: border-box; }
  html, body {
    width: 1200px;
    height: 1000px;
    overflow: hidden;
    background: var(--backdrop);
    font-family: "Poppins", sans-serif;
  }
  .canvas { position: relative; width: 1200px; height: 1000px; }

  .card { position: absolute; overflow: hidden; }

  /* Front */
  .card--front {
    left: 299px; top: 111px; width: 602px; height: 344px;
    background: var(--paper);
    color: var(--ink);
  }
  .front-brand {
    position: absolute; left: 38px; top: 0; height: 344px;
    display: flex; align-items: center; gap: 12px;
  }
  .front-brand__dot {
    width: 16px; height: 16px; border-radius: 50%;
    background: var(--ink);
  }
  .front-brand__name {
    font-weight: 600; font-size: 26px; line-height: 1.15;
    letter-spacing: 1px; text-transform: uppercase;
  }
  .contact {
    position: absolute; left: 256px; width: 300px; top: 98px;
    text-align: center; text-transform: uppercase;
  }
  .contact__name { font-weight: 600; font-size: 17px; letter-spacing: 0.3px; line-height: 22px; }
  .contact__role { font-weight: 500; font-size: 14px; line-height: 18px; }
  .contact__lines { margin-top: 46px; font-weight: 400; font-size: 15px; letter-spacing: 1px; line-height: 26px; white-space: nowrap; }
  .contact__lines b { font-weight: 600; }

  /* Back */
  .card--back {
    left: 298px; top: 517px; width: 605px; height: 345px;
    background: var(--ink);
    color: var(--reverse-ink);
    display: flex; align-items: center; justify-content: center;
  }
  .back-brand { display: flex; align-items: center; gap: 22px; }
  .back-brand__dot {
    width: 22px; height: 22px; border-radius: 50%;
    background: var(--reverse-ink);
  }
  .back-brand__name {
    font-weight: 300; font-size: 44px; line-height: 1.05;
    letter-spacing: 4px; text-transform: uppercase;
  }
</style>
</head>
<body>
<main class="canvas">
  <section class="card card--front" aria-label="Business card front">
    <div class="front-brand">
      <span class="front-brand__dot"></span>
      <span class="front-brand__name">MP<br>Frameworks</span>
    </div>
    <div class="contact">
      <p class="contact__name">Miles Perrow</p>
      <p class="contact__role">Photographer</p>
      <div class="contact__lines">
        <p>07812 593174</p>
        <p>miles@<b>mpframeworks</b>.co.uk</p>
        <p><b>mpframeworks</b>.co.uk</p>
      </div>
    </div>
  </section>

  <section class="card card--back" aria-label="Business card back">
    <div class="back-brand">
      <span class="back-brand__dot"></span>
      <span class="back-brand__name">MP<br>Frameworks</span>
    </div>
  </section>
</main>
</body>
</html>
```